Fun modern label needed for olive oil bottle

I need a label for a boutique handmade olive oil line. It needs to be fun and reflect the smallness of the operation and from rural Australia

The name of the line comes from the fact that I live in rural Australia and the black tar road ends 5 km from my home. The road turns to dusty slippery gravel in summer and wet and slippery gravel mud in winter.
Those of us who live out here say that the best people live WATTLE CREEK HOLLOW.

There are no restrictions on colours but it MUST be fun with clear strong lines.

The label is rectangular with the short sides top and bottom. I shall measure the bottles later today and update the brief for you

Below is an example of the bottles used and there will be 3 different sizes
Updates

I have added a couple of photos to show Australian labels and what is need on them sorry to have left out this crucial information

Industry/Entity Type

Boutique

Requirements
Must have
• Wattle Creek Hollow as name
Some sort of logo

```html
<!DOCTYPE html>
<html lang="en">
<head>
<meta charset="utf-8">
<title>Wattle Creek Hollow – Extra Virgin Olive Oil Label</title>
<link rel="stylesheet" href="https://fonts.googleapis.com/css2?family=Federo&family=Pinyon+Script&family=Special+Elite&family=Cormorant+Garamond:wght@500&display=swap">
<style>
  :root {
    --page-bg: #ffffff;
    --label-bg: #2a2828;
    --label-edge: #d98a2a;
    --brand-cream: #f3e3c7;
    --text-light: #f4f1ec;
    --frame-white: #ffffff;
    --frame-line: #8a8a8a;
    --art-dark: #3a3a3a;
    --art-soil: #d9a86a;
  }
  html, body {
    margin: 0;
    padding: 0;
    width: 1200px;
    height: 991px;
    overflow: hidden;
    background: var(--page-bg);
  }
  .canvas {
    position: relative;
    width: 1200px;
    height: 991px;
  }
  .label {
    position: absolute;
    left: 418px;
    top: 45px;
    width: 363px;
    height: 900px;
  }
  .label-shape {
    position: absolute;
    inset: 0;
  }
  .brand-line {
    position: absolute;
    margin: 0;
    font-family: "Special Elite", monospace;
    font-size: 30px;
    line-height: 1;
    color: var(--brand-cream);
  }
  .brand-line--first { left: 58px; top: 83px; }
  .brand-line--second { left: 73px; top: 124px; }
  .brand-line--third { left: 139px; top: 161px; }
  .art-frame {
    position: absolute;
    left: 74px;
    top: 199px;
    width: 216px;
    height: 338px;
    box-sizing: border-box;
    background: var(--frame-white);
    padding: 9px;
  }
  .art-frame__inner {
    width: 100%;
    height: 100%;
    box-sizing: border-box;
    border: 1px solid var(--frame-line);
    padding: 4px;
  }
  .art-illustration {
    width: 100%;
    height: 100%;
    background: linear-gradient(to bottom,
      #ffffff 0%, #ffffff 8%, #2c2c2c 20%, #2c2c2c 42%,
      var(--art-dark) 45%, #4a4a4a 60%, var(--art-soil) 64%,
      #c9935a 85%, #ffffff 100%);
  }
  .product-name, .product-grade, .product-origin, .product-volume {
    position: absolute;
    left: 0;
    width: 100%;
    margin: 0;
    text-align: center;
    color: var(--text-light);
    line-height: 1;
  }
  .product-name {
    top: 600px;
    font-family: "Federo", sans-serif;
    font-size: 52px;
  }
  .product-grade {
    top: 670px;
    font-family: "Federo", sans-serif;
    font-size: 28px;
  }
  .product-origin {
    top: 786px;
    font-family: "Pinyon Script", cursive;
    font-size: 26px;
  }
  .product-volume {
    top: 874px;
    font-family: "Cormorant Garamond", serif;
    font-weight: 500;
    font-size: 12px;
    letter-spacing: 0.5px;
  }
</style>
</head>
<body>
  <div class="canvas">
    <section class="label">
      <svg class="label-shape" width="363" height="900" viewBox="0 0 363 900" aria-hidden="true">
        <path d="M21,1 H342 A20,20 0 0 0 362,21 V879 A20,20 0 0 0 342,899 H21 A20,20 0 0 0 1,879 V21 A20,20 0 0 0 21,1 Z"
              fill="var(--label-bg)" stroke="var(--label-edge)" stroke-width="2"/>
      </svg>

      <p class="brand-line brand-line--first">Wattle</p>
      <p class="brand-line brand-line--second">Creek</p>
      <p class="brand-line brand-line--third">Hollow</p>

      <div class="art-frame">
        <div class="art-frame__inner">
          <div class="art-illustration" role="img" aria-label="Illustration of a lone tree above ground with its roots spreading down through dark earth and a layer of golden gravel soil"></div>
        </div>
      </div>

      <h1 class="product-name">Olive Oil</h1>
      <p class="product-grade">Extra Virgin</p>
      <p class="product-origin">Australia</p>
      <p class="product-volume">250 ML</p>
    </section>
  </div>
</body>
</html>
```